Cover für den Roman Marlene betritt die Bühne
Zielgruppe
Autorin einer belletristischen Erzählung über die Kunst der Moderne. Das Buch richtet sich an Leser die sich für Moderne Kunst interessieren.
Aufgabenstellung
Gesucht wird ein sehr zeitgemäßes und auffallendes Design, auch gerne mit einer starken Hintergrundfarbe. Der Leser soll auf den ersten Blick erkennen können, dass es hier um Kunst geht (Lorenz Aubach, Tarnowski, Ferrandi Hadley, etc). Bitte unbedingt alle Lizenzrechte abklären und keine Originalwerke verwenden.
Eine Idee wäre einen Bezug zu "Marlene und der Barastides" herzustellen. (Vielzitiertes Thema in der Kunstgeschichte, Marlene schlägt dem Feldherrn Barastides den Kopf ab und befreit ihr Volk.)
Das Design sollte aber trotzdem nett und nicht gruselig sein.
Ganz wichtig keine nackte Marlene. Sie ist stark und emanzipiert sich!
Text auf der Vorderseite:
Olga Mertelhuber
Marlene betritt die Bühne
Erzählung über die Kunst der Moderne
Text auf der Rückseite:
kurze Inhaltsangabe
Das Cover soll für ein Taschenbuch als auch ein e-book funktionieren

```html
<!DOCTYPE html>
<html lang="de">
<head>
<meta charset="utf-8">
<title>Marlene betritt die Bühne – Olga Mertelhuber</title>
<link rel="stylesheet" href="https://fonts.googleapis.com/css2?family=Open+Sans:wdth,wght@75..100,400..800&display=swap">
<style>
  :root {
    --paper: #f3f4f0;
    --orchid: #c45fb6;
    --plum: #7a2c78;
    --title-plum: #6e2468;
    --author-pink: #c2509f;
  }
  html, body {
    margin: 0;
    padding: 0;
    overflow: hidden;
    background: var(--paper);
  }
  .cover {
    position: relative;
    width: 749px;
    height: 1200px;
    background: var(--paper);
    overflow: hidden;
    font-family: "Open Sans", Arial, sans-serif;
  }
  .cover-art {
    position: absolute;
    left: 90px;
    top: 24px;
    width: 600px;
    height: 870px;
  }
  .text-block {
    position: absolute;
    right: 36px;
    top: 872px;
    text-align: right;
  }
  .author {
    margin: 0;
    color: var(--author-pink);
    font-size: 31px;
    font-weight: 600;
    letter-spacing: 2.5px;
    text-transform: uppercase;
    line-height: 1;
  }
  .title {
    margin: 12px 0 0;
    color: var(--title-plum);
    font-size: 68px;
    font-weight: 700;
    font-stretch: 75%;
    text-transform: uppercase;
    line-height: 1.02;
    letter-spacing: 0.5px;
  }
  .title span { display: block; }
  .subtitle {
    margin: 10px 0 0;
    color: var(--author-pink);
    font-size: 21px;
    font-weight: 600;
    letter-spacing: 1.6px;
    text-transform: uppercase;
    line-height: 1;
  }
</style>
</head>
<body>
  <main class="cover">
    <svg class="cover-art" viewBox="0 0 600 870" preserveAspectRatio="none" role="img" aria-label="Illustration: zwei ineinander verschlungene Figuren in Orchideenrosa und Pflaumenviolett, als Linolschnitt angelegt">
      <defs>
        <linearGradient id="figure-tones" x1="0" y1="0" x2="1" y2="0">
          <stop offset="0" stop-color="var(--orchid)"/>
          <stop offset="0.52" stop-color="var(--orchid)"/>
          <stop offset="0.56" stop-color="var(--plum)"/>
          <stop offset="1" stop-color="var(--plum)"/>
        </linearGradient>
      </defs>
      <path d="M120 20 C40 60 0 190 0 350 C0 560 60 760 150 835 C200 865 270 840 300 800 L520 840 C560 820 595 770 585 710 C565 560 545 390 505 240 C475 130 435 55 385 28 C300 0 200 0 120 20 Z" fill="url(#figure-tones)"/>
    </svg>

    <header class="text-block">
      <p class="author">Olga Mertelhuber</p>
      <h1 class="title"><span>Marlene betritt</span><span>die Bühne</span></h1>
      <p class="subtitle">Erzählung über die Kunst der Moderne</p>
    </header>
  </main>
</body>
</html>
```